Plakat-Design für LACH-TRANCE-ABEND
Zielgruppe
Ich bin Hypnotiseur und trete europaweit bei div. Events mit meiner LACH-TRANCE-ABEND auf (www.lach-trance-abend.example)
Aufgabenstellung
Das Plakat sollte die Elemente Hypnose+Comedy darstellen. Es wird für ein renommiertes Theater gebraucht für deren Leuchtkästen im Format: TIFF/PSD (alternativ JPG) 594mm x 840mm + 1mm Beschnitt.
Das Plakat sollte unten ein freies Störerfeld haben, damit dieses auch für zukünftige Gastspiele genutzt werden kann.
INFOS auf dem Plakat:
-Künstlername (=Varomir)
-Lach-Trance-Abend
-echte Live-Hypnose
Die Show heisst "Träum!" (wie auf einigen Bildern von mir ja dargestellt)
Das Plakat sollte eine gewisse Wertigkeit vermitteln, etwas exklusives, einmaliges. Die Show ist für Erwachsene, daher kein kindliches, zu verspieltes Design. Lieber klar und exklusiv, hochwertig. Danke!

```html
<!DOCTYPE html>
<html lang="de">
<head>
<meta charset="utf-8">
<title>Träum! – Varomir – Plakat</title>
<link href="https://fonts.googleapis.com/css2?family=Cinzel:wght@400;500&family=Cormorant+Garamond:wght@300;400&display=swap" rel="stylesheet">
<style>
  :root {
    --stage: #16151c;
    --night: #1b1230;
    --violet: #3a2463;
    --haze: #d9d3e6;
    --lilac: #a58fc9;
    --rose: #eaa9cf;
    --rose-deep: #c974a8;
    --text-soft: #d8cde8;
    --text-dim: #a898c2;
    --gold: #e9cf86;
  }
  * { margin: 0; padding: 0; box-sizing: border-box; }
  html, body {
    width: 1200px; height: 797px; overflow: hidden;
    background: var(--stage);
  }
  .poster {
    position: absolute; left: 332px; top: 18px;
    width: 537px; height: 761px; overflow: hidden;
    background: linear-gradient(180deg, var(--violet) 0%, var(--night) 100%);
    font-family: "Cinzel", serif;
    color: var(--text-soft);
    text-align: center;
  }
  .portrait {
    position: absolute; inset: 0 0 auto 0; height: 560px;
    background:
      radial-gradient(ellipse 34% 40% at 50% 38%, #b88f86 0%, rgba(184,143,134,0) 100%),
      radial-gradient(ellipse 70% 80% at 50% 42%, var(--haze) 0%, #bdb3d3 55%, rgba(58,36,99,0) 100%),
      linear-gradient(180deg, #e6e2ee 0%, #9f8cc2 70%, var(--violet) 100%);
  }
  .portrait-fade {
    position: absolute; left: 0; right: 0; top: 330px; height: 431px;
    background:
      radial-gradient(ellipse 40% 50% at 55% 70%, rgba(110,80,200,.35) 0%, rgba(110,80,200,0) 100%),
      linear-gradient(180deg, rgba(27,18,48,0) 0%, rgba(40,26,75,.85) 35%, var(--night) 100%);
  }
  .artist {
    position: absolute; top: 450px; left: 0; right: 0;
    font-size: 28px; line-height: 34px; font-weight: 400; letter-spacing: 2px;
    color: var(--text-soft);
  }
  .show-title {
    position: absolute; top: 500px; left: 0; right: 0;
    font-family: "Cormorant Garamond", serif; font-weight: 300;
    font-size: 108px; line-height: 1; letter-spacing: 4px;
    color: var(--rose);
  }
  .claims {
    position: absolute; top: 620px; left: 50px; right: 50px;
    display: flex; justify-content: space-between;
    font-size: 12.5px; line-height: 16px; letter-spacing: 2px; color: var(--text-soft);
  }
  .blurb {
    position: absolute; top: 642px; left: 0; right: 0;
    font-family: "Cormorant Garamond", serif;
    font-size: 8.5px; line-height: 12px; letter-spacing: .6px;
    color: var(--text-dim); text-transform: uppercase;
  }
  .brand {
    position: absolute; top: 688px; left: 0; right: 0;
    display: flex; justify-content: center; align-items: center; gap: 5px;
    font-size: 9px; line-height: 12px; letter-spacing: 1px; color: var(--text-soft);
  }
  .brand-dot {
    width: 9px; height: 9px; border-radius: 50%;
    border: 1px solid var(--text-soft);
  }
  .web {
    position: absolute; top: 712px; left: 0; right: 0;
    font-size: 9px; line-height: 12px; letter-spacing: 1.5px; color: var(--gold);
    text-transform: uppercase;
  }
  .footnote {
    position: absolute; top: 740px; left: 0; right: 0;
    font-family: "Cormorant Garamond", serif;
    font-size: 7.5px; line-height: 10px; letter-spacing: 1px; color: var(--text-dim);
    text-transform: uppercase;
  }
</style>
</head>
<body>
  <main class="poster">
    <div class="portrait" role="img" aria-label="Porträtfoto des Hypnotiseurs vor hellen konzentrischen Hypnose-Spiralen"></div>
    <div class="portrait-fade" role="img" aria-label="Violetter Sternennebel, der das Porträt nach unten ausblendet"></div>

    <p class="artist">VAROMIR</p>
    <h1 class="show-title">TRÄUM</h1>

    <div class="claims">
      <span>LACH-TRANCE-ABEND</span>
      <span>ECHTE LIVE-HYPNOSE</span>
    </div>

    <p class="blurb">
      Ein einzigartiger Abend, den Ihre Gäste so schnell nicht vergessen werden.<br>
      So etwas haben Sie sicher noch nie gesehen und erlebt.<br>
      Staunen, Lachen und erstklassige Unterhaltung live.
    </p>

    <div class="brand"><span class="brand-dot"></span><span>VAROMIR</span></div>

    <p class="web">www.lach-trance-abend.example</p>

    <p class="footnote">Vorverkauf an allen bekannten Vorverkaufsstellen und an der Abendkasse</p>
  </main>
</body>
</html>
```